Flyer-Design für ein Hautkrebs-Präventionsprojekt
Zielgruppe
Wir sind der Lindenhilfe Westerau-Sommerfeld. Bei diesem Projekt handelt es sich um ein Hautkrebs-Präventionsprojekt. Ein gesunder Umgang mit der Sonne soll vor allem bei Kindern, aber auch ihren Eltern und Erzieherinnen gefördert werden. Durch die sensible Kinderhaut (Schutzmechanismus noch nicht ganz entwickelt) sind Sonnenbrände im Kindheitsalter ein extremes Hautkrebsrisiko für das spätere Erwachsenenalter. Um über Möglichkeiten wie man sich schützen kann und einen gesunden Umgang mit der Sonne zu pflegen bieten wir Informationsschulungen an. Hierfür sollen die Flyer gestaltet werden.
Aufgabenstellung
Die Flyer in A6, also Postkartenformat (hoch oder quer spielt keine Rolle) sollen sich an Eltern und pädagogisches Fachpersonal richten. Unsere Vorstellung/Idee war ein 'pfiffiger', eventuell herausfordender aber auch lustiger Satz vorne, und die Einladung hinten. Inspiriert so ein bisschen von diversen Werbekarten die man in Clubs oder in der Gastronomie mitnehmen kann! Die Vorderseite soll also Aufmerksamkeit an sich ziehen und zum 'in die Hand nehmen und einpacken' bewegen.
Ansonsten ist Ihrer Kreativität keine Grenzen gesetzt.
Als Einladung soll folgender Text auf die Rückseite (inkl. Logo):
Liebe Eltern, liebe pädagogische Fachkräfte,
wir laden sie herzlich zu unserer Informationsveranstaltung über einen gesunden Umgang mit der Sonne zur Hautkrebsprävention ein.
Wann? 11.04.19 o. 11.06.19
Wo? Allgemeine Vorsorgekasse Westerau-Sommerfeld
Hollerbusch-Weg 218
70629 Stuttgart
Besonders Kinder haben aufgrund ihrer sensiblen Haut ein erhöhtes Schutzbedürfnis.
Nutzen Sie die Chance, sich zu informieren und Ihre Familie und sich zu schützen!
Haben Sie noch Fragen? Melden Sie sich bei uns
Gerne können anstatt wann und wo und für die Kontaktdaten kleine Symbole verwendet werden.
Wir freuen uns auf Ihre Vorschläge!
PS: Die 'Wann'-Daten können sich eventuell noch ändern

```html
<!DOCTYPE html>
<html lang="de">
<head>
<meta charset="utf-8">
<title>Lindenhilfe Westerau-Sommerfeld – Flyer Hautkrebsprävention</title>
<link rel="stylesheet" href="https://fonts.googleapis.com/css2?family=Lato:wght@300;400;700;900&family=Open+Sans:wght@700;800&family=Alegreya+Sans+SC:wght@400&display=swap">
<style>
  :root {
    --green: #6aa84f;
    --green-dark: #5a9a40;
    --ink: #111111;
    --text: #2a2a2a;
    --white: #ffffff;
    --stage: #ffffff;
    --shadow: rgba(0,0,0,0.22);
    --sky: #bcdfe8;
  }
  * { box-sizing: border-box; margin: 0; padding: 0; }
  html, body { width: 1200px; height: 848px; overflow: hidden; background: var(--stage); }
  .stage { position: relative; width: 1200px; height: 848px; }
  .card {
    position: absolute; top: 126px; width: 429px; height: 606px;
    background: var(--white); box-shadow: 0 0 4px var(--shadow); overflow: hidden;
  }
  .card--front { left: 143px; }
  .card--back { left: 642px; }

  .brand { position: absolute; left: 16px; top: 12px; display: flex; align-items: flex-end; gap: 7px; }
  .brand__mark { width: 26px; height: 26px; background: var(--green); margin-bottom: 2px; }
  .brand__name {
    font-family: "Alegreya Sans SC", sans-serif; font-weight: 400; font-size: 15px;
    line-height: 17px; letter-spacing: 1.2px; color: var(--ink);
  }
  .header-rule { position: absolute; left: 0; top: 70px; width: 100%; height: 2px; background: rgba(0,0,0,0.1); }

  .photo {
    position: absolute; left: 0; top: 71px; width: 429px; height: 371px;
    background:
      radial-gradient(ellipse at 50% 55%, #f4f2ef 0 22%, transparent 42%),
      radial-gradient(ellipse at 20% 85%, #c7b8e0 0 10%, transparent 30%),
      radial-gradient(ellipse at 85% 80%, #e9e6a8 0 8%, transparent 26%),
      linear-gradient(180deg, #bfe0ea 0%, #b6d9e5 55%, #a9c9e0 100%);
  }

  .badge {
    position: absolute; border-radius: 50%; display: flex; align-items: center; justify-content: center;
    font-family: "Open Sans", sans-serif; font-weight: 800; text-align: center;
  }
  .badge--front {
    left: 285px; top: 20px; width: 122px; height: 122px;
    background: var(--green); border: 3px solid var(--white); box-shadow: 0 0 3px var(--shadow);
    color: var(--white); font-size: 17px; line-height: 19px;
  }
  .badge--back {
    left: 261px; top: 350px; width: 122px; height: 122px;
    background: var(--white); box-shadow: 0 0 4px var(--shadow);
    color: var(--green); font-size: 17px; line-height: 18px; z-index: 2;
  }
  .badge span { transform: rotate(-6deg); display: block; }

  .headline {
    position: absolute; left: 36px; top: 455px; font-family: "Lato", sans-serif; font-weight: 900;
    font-size: 35px; line-height: 35px; letter-spacing: -1.2px; color: var(--green);
  }
  .headline__line2 { padding-left: 12px; display: block; }

  .front-footer { position: absolute; left: 49px; right: 40px; top: 570px; display: flex; align-items: center; justify-content: space-between; }
  .web { font-family: "Lato", sans-serif; font-weight: 700; font-size: 14px; color: var(--ink); }
  .sponsors { display: flex; gap: 12px; }
  .sponsor { font-family: "Lato", sans-serif; font-weight: 700; font-size: 11px; color: #1d4e8f; }

  .letter { position: absolute; left: 50px; right: 40px; top: 96px; font-family: "Lato", sans-serif; color: var(--text); font-size: 14px; line-height: 18.8px; }
  .letter p { margin-bottom: 15.5px; font-weight: 300; }
  .letter b { font-weight: 700; color: var(--ink); }
  .letter .salutation { font-weight: 700; color: var(--ink); margin-bottom: 15px; }
  .letter .callout { font-weight: 700; color: var(--green); margin-bottom: 18px; }
  .letter .web { display: block; margin-top: 14px; }

  .event {
    position: absolute; left: 0; top: 443px; width: 100%; height: 163px; background: var(--green);
    color: var(--white); font-family: "Lato", sans-serif; padding: 12px 0 0 50px;
  }
  .event__date { font-weight: 900; font-size: 34px; line-height: 38px; letter-spacing: -0.3px; }
  .event__time { font-weight: 700; font-size: 18px; margin-top: 5px; }
  .event__place { font-weight: 400; font-size: 13.5px; line-height: 19px; margin-top: 2px; }
  .event__arrow { position: absolute; left: 225px; top: 34px; }
</style>
</head>
<body>
<main class="stage">

  <section class="card card--front">
    <div class="brand">
      <div class="brand__mark"></div>
      <div class="brand__name">Lindenhilfe<br>Westerau-Sommerfeld</div>
    </div>
    <div class="header-rule"></div>
    <div class="photo" role="img" aria-label="Foto: Dalmatinerwelpe mit bunten Farbflecken im Fell, liegend auf farbbespritzter Fläche mit Pinsel und pastellfarbenen Eiern vor hellblauem Hintergrund"></div>
    <div class="badge badge--front"><span>Schütze<br>Dich<br>und Deine<br>Haut!</span></div>
    <h1 class="headline">„DIE MEISTEN FLECKEN<span class="headline__line2">SIND HARMLOS.“</span></h1>
    <footer class="front-footer">
      <span class="web">www.lindenhilfews.de</span>
      <div class="sponsors">
        <span class="sponsor">Vitakasse</span>
        <span class="sponsor">Nordtal Bank</span>
      </div>
    </footer>
  </section>

  <section class="card card--back">
    <div class="brand">
      <div class="brand__mark"></div>
      <div class="brand__name">Lindenhilfe<br>Westerau-Sommerfeld</div>
    </div>
    <div class="header-rule"></div>
    <div class="letter">
      <p class="salutation">Liebe Eltern, liebe pädagogische Fachkräfte,</p>
      <p>besonders Kinder haben aufgrund ihrer sensiblen Haut ein erhöhtes Schutzbedürfnis.<br>
      Aus diesem Grund laden wir Sie herzlich zu einem unserer zwei <b>Informationsveranstaltungen</b> über einen gesunden Umgang mit der Sonne zur <b>Hautkrebsprävention</b> ein.</p>
      <p class="callout">Nutzen Sie die Chance, sich zu informieren und Ihre Familie und sich zu schützen!</p>
      <p><b>Haben Sie noch Fragen?</b><br>Melden Sie sich bei uns unter:<br>0711/555-20480 oder<br>info@lindenhilfews.de</p>
      <span class="web">www.lindenhilfews.de</span>
    </div>
    <div class="badge badge--back"><span>Wählen<br>Sie zwischen<br>zwei<br>Terminen.</span></div>
    <div class="event">
      <div class="event__date">11.04.2019</div>
      <div class="event__date">11.06.2019</div>
      <svg class="event__arrow" width="70" height="45" viewBox="0 0 70 45" aria-hidden="true">
        <path d="M64 2 C62 28 38 40 10 28" fill="none" stroke="#ffffff" stroke-width="3" stroke-linecap="round"/>
        <path d="M2 22 L20 18 L12 40 Z" fill="#ffffff"/>
      </svg>
      <div class="event__time">Veranstaltungsbeginn: 18:30 Uhr</div>
      <div class="event__place">Allgemeine Vorsorgekasse Westerau-Sommerfeld<br>Hollerbusch-Weg 218 | 70629 Stuttgart</div>
    </div>
  </section>

</main>
</body>
</html>
```